Business acrd and Stationery desgin FOR HARLOW

I want creative and expressive stationary design .on the front side for business card I need the logo and doctors name to be there and on the back side I need time and appointment .Please see attached business card to use same names ,but use address below and phone number

Note:the deigner must submit the file in vector format and PSD and PDF

Business name is :Harlow Crest Medical Clinic.

Address:
20485 57 ST NW
City :EDMONTON AB
Postal code: T6K 3P8

Phone :(780) 492-3815
Fax:(780) 492-5127

Other Business name :Harlow Medical Clinic

• logo in the back on business card

```html
<!DOCTYPE html>
<html lang="en">
<head>
<meta charset="utf-8">
<title>Harlow Crest Medical Clinic – Business Card</title>
<link rel="stylesheet" href="https://fonts.googleapis.com/css2?family=Marcellus&family=Tinos&display=swap">
<style>
  :root {
    --page: #eceff1;
    --card-body: #e3f1f7;
    --card-glow: #eef7fb;
    --steel: #467e9c;
    --red: #ec3636;
    --peach: #f5c0ad;
    --teal: #5bb5ad;
    --teal-dark: #46a39b;
    --teal-light: #7cccc6;
    --sky: #4bbfe4;
    --sky-light: #8dd4ec;
    --mist: #c9d6e0;
    --navy: #1d3f94;
    --ink: #555c63;
    --rule: #8a8f94;
  }
  * { box-sizing: border-box; margin: 0; padding: 0; }
  html, body { width: 1200px; height: 1000px; overflow: hidden; background: var(--page); }
  .canvas { position: relative; width: 1200px; height: 1000px; }

  .card {
    position: absolute; left: 250px; width: 700px; height: 400px;
    background: var(--card-body); overflow: hidden;
    box-shadow: 0 4px 14px rgba(0,0,0,.12);
  }
  .card--front { top: 70px; }
  .card--back { top: 530px; }
  .card__texture { position: absolute; inset: 0; }
  .card--front .card__texture { background: radial-gradient(ellipse at 85% 70%, var(--card-glow), var(--card-body) 60%); }
  .card--back .card__texture { background: radial-gradient(ellipse at 90% 20%, var(--card-glow), var(--card-body) 60%); }
  .block { position: absolute; }

  /* front */
  .brand { position: absolute; left: 140px; top: 120px; display: flex; align-items: center; gap: 26px; }
  .brand__dot { width: 92px; height: 92px; border-radius: 50%; background: var(--red); flex: none; }
  .brand__name {
    font-family: "Marcellus", serif; color: var(--navy);
    font-size: 38px; line-height: 1.08; letter-spacing: .5px; text-transform: uppercase;
  }
  .tagline {
    position: absolute; left: 258px; top: 232px; width: 380px;
    display: flex; align-items: center; gap: 12px;
    font-family: "Marcellus", serif; font-size: 18px; letter-spacing: 4px; color: var(--rule);
  }
  .tagline::before, .tagline::after { content: ""; flex: 1; height: 2px; background: var(--rule); }

  /* back */
  .doctors {
    position: absolute; right: 60px; top: 70px; text-align: right;
    font-family: "Tinos", serif; font-size: 30px; line-height: 1.15; color: var(--red);
  }
  .field { position: absolute; left: 60px; right: 52px; display: flex; align-items: flex-end;
    font-family: "Tinos", serif; font-size: 27px; letter-spacing: 1px; color: var(--ink); }
  .field__label { width: 290px; }
  .field__line { flex: 1; border-bottom: 2px solid var(--rule); margin-bottom: 8px; }
  .field--time { top: 168px; }
  .field--appt { top: 202px; }
  .field--blank { top: 254px; height: 2px; border-bottom: 2px solid var(--rule); }
  .address, .contact {
    position: absolute; top: 280px; font-family: "Tinos", serif; font-size: 15px;
    line-height: 1.2; color: var(--ink); letter-spacing: .5px;
  }
  .address { left: 60px; }
  .contact { right: 52px; text-align: right; }
</style>
</head>
<body>
<main class="canvas">

  <section class="card card--front" aria-label="Card front">
    <div class="card__texture" role="img" aria-label="Faint curved line background texture"></div>
    <div class="block" style="left:0;top:0;width:160px;height:42px;background:var(--teal-dark)"></div>
    <div class="block" style="left:160px;top:0;width:540px;height:42px;background:var(--sky-light)"></div>
    <div class="block" style="left:0;top:42px;width:160px;height:12px;background:var(--red)"></div>
    <div class="block" style="left:0;top:54px;width:160px;height:90px;background:var(--peach)"></div>
    <div class="block" style="left:0;top:144px;width:160px;height:90px;background:var(--mist)"></div>
    <div class="block" style="left:0;top:234px;width:160px;height:80px;background:#d2e4e8"></div>
    <div class="block" style="left:0;top:340px;width:160px;height:60px;background:var(--teal-light)"></div>
    <div class="block" style="left:160px;top:340px;width:540px;height:60px;background:var(--sky-light)"></div>

    <div class="brand">
      <span class="brand__dot"></span>
      <p class="brand__name">Harlow Crest<br>Medical Clinic</p>
    </div>
    <p class="tagline">WE CARE</p>
  </section>

  <section class="card card--back" aria-label="Card back">
    <div class="card__texture" role="img" aria-label="Faint curved line background texture"></div>
    <div class="block" style="left:0;top:0;width:175px;height:40px;background:var(--steel)"></div>
    <div class="block" style="left:175px;top:0;width:175px;height:40px;background:var(--red)"></div>
    <div class="block" style="left:350px;top:0;width:175px;height:40px;background:var(--teal)"></div>
    <div class="block" style="left:525px;top:0;width:175px;height:40px;background:var(--sky)"></div>
    <div class="block" style="left:0;top:40px;width:175px;height:18px;background:var(--mist)"></div>
    <div class="block" style="left:175px;top:40px;width:175px;height:18px;background:var(--peach)"></div>
    <div class="block" style="left:350px;top:40px;width:175px;height:18px;background:#bfe3e0"></div>
    <div class="block" style="left:525px;top:40px;width:175px;height:18px;background:#bde6f3"></div>

    <p class="doctors">Dr A Venholt<br>Dr Z Marisol</p>

    <div class="field field--time"><span class="field__label">TIME</span><span class="field__line"></span></div>
    <div class="field field--appt"><span class="field__label">APPOINTMENT</span><span class="field__line"></span></div>
    <div class="field field--blank"></div>

    <p class="address">20485 57 ST NW<br>EDMONTON AB<br>T6K 3P8</p>
    <p class="contact">Phone:(780) 492-3815<br>Fax:(780) 492-5127</p>

    <div class="block" style="left:0;top:352px;width:175px;height:48px;background:var(--teal-light)"></div>
    <div class="block" style="left:175px;top:352px;width:175px;height:48px;background:var(--teal)"></div>
    <div class="block" style="left:350px;top:352px;width:175px;height:48px;background:var(--sky-light)"></div>
    <div class="block" style="left:525px;top:352px;width:175px;height:48px;background:var(--teal-dark)"></div>
  </section>

</main>
</body>
</html>
```